Funken-und-Fragen Flyer
Zielgruppe
Eltern, die ihre Kinder in ihrer Entwicklung fördern möchten.
Aufgabenstellung
Wir organisieren eine Messe mit dem Thema "Funken und Fragen". Bei der Messe geht es nicht um das Lernen über Bücher (alleine) oder das Schulische, sondern die Messe soll für Eltern sein, die ihre Kinder fördern möchten durch die Behebung von Lernblockaden, Förderung der Konzentration, Kreativität, spielerisches Lernen etc. Es geht um Kinder ab ca. 4 Jahren.
Als Aussteller werden verschiedene Themen angesprochen: Kinesiologie, Logopädie, Privatschulen mit speziellem Angenbot, Schachunterricht, spielerisches Lernangebot, Kindermalen etc. , alles was darauf zielt, Kreativität und Lernen bei Kindern zu fördern.
Wir brauchen daher einen Flyer, der die Eltern anspricht. Die Messe findet am Sonntag, 9.11.2012 statt. Beginn 11 Uhr, Ende 18.00 Uhr. Ort: Seeforumhalle - Lindensaal, Wendelgasse 7, 8047 Zürich.
Das Logo wird attached. Das Format ist frei wählbar.

```html
<!DOCTYPE html>
<html lang="de">
<head>
<meta charset="utf-8">
<title>Funken und Fragen – Messe Zürich</title>
<link rel="stylesheet" href="https://fonts.googleapis.com/css2?family=Nunito:wght@800;900&family=Open+Sans:wght@400;700&family=Space+Mono:wght@700&display=swap">
<style>
:root{
  --bg:#4a4a4a;
  --orange:#f39200;
  --orange-light:#f6a623;
  --purple:#8c1c7c;
  --blue:#1a9bd7;
  --teal:#0e9a96;
  --white:#ffffff;
  --grey:#5b5b5b;
  --photo-warm:#c9b79c;
  --photo-yellow:#f3c21a;
}
*{box-sizing:border-box;margin:0;padding:0}
html,body{width:1200px;height:910px;overflow:hidden;background:var(--bg)}
body{position:relative;font-family:"Open Sans",sans-serif}
.piece{position:absolute;overflow:hidden;background:var(--white)}
.abs{position:absolute}
.mono{font-family:"Space Mono",monospace;font-weight:700}

/* Poster */
.poster{left:25px;top:45px;width:560px;height:775px}
.poster .header{left:0;top:0;width:560px;height:245px;background:var(--orange-light)}
.poster .amp{left:230px;top:-40px;font-family:"Nunito",sans-serif;font-weight:900;font-size:330px;line-height:1;color:rgba(255,255,255,.35)}
.poster .title{left:20px;top:62px;font-family:"Nunito",sans-serif;font-weight:900;font-size:70px;line-height:1;color:var(--purple);letter-spacing:-1px}
.poster .subtitle{left:22px;top:132px;font-size:30px;color:var(--white)}
.photo-cool{background:linear-gradient(135deg,#8a8a84,var(--photo-warm))}
.photo-sun{background:linear-gradient(135deg,var(--photo-yellow),#e59a12)}
.brand{display:flex;flex-direction:column;align-items:center;justify-content:center;background:var(--white)}
.brand .dot{width:34px;height:34px;border-radius:50%;background:var(--grey);margin-bottom:12px}
.brand .name{font-family:"Open Sans",sans-serif;font-size:21px;color:var(--teal)}
.brand .url{font-size:9px;color:var(--grey);margin-top:2px}
.poster .info{left:0;top:418px;width:560px;height:187px;background:var(--purple);color:var(--white)}
.poster .date{left:37px;top:18px;font-size:40px}
.poster .time{left:37px;top:82px;font-size:21px;font-weight:700}
.poster .place{left:37px;top:112px;font-size:16px;line-height:1.5}
.poster .claim{left:0;top:605px;width:560px;height:68px;background:var(--white)}
.poster .claim p{position:absolute;left:33px;top:20px;font-size:13px;font-weight:700;color:var(--purple);line-height:1.5}
.poster .footer{left:0;top:673px;width:560px;height:102px;background:var(--orange);color:var(--white);font-size:14px;font-weight:700;line-height:1.8;padding:28px 36px}
.pill{position:absolute;width:155px;height:54px;border-radius:27px 0 0 27px;transform:rotate(-20deg);color:var(--white);font-weight:700;font-size:14px;line-height:1.2;display:flex;align-items:center;justify-content:center;text-align:center}
.pill.blue{background:var(--blue)}
.pill.orange{background:var(--orange)}
.pill.teal{background:var(--teal)}

/* Banner */
.banner{left:612px;top:173px;width:466px;height:228px}
.banner .band{left:0;top:130px;width:466px;height:98px;background:var(--purple)}
.banner .band .top{position:absolute;left:28px;top:8px;font-size:36px;color:var(--white)}
.banner .band .bottom{position:absolute;left:142px;top:55px;font-size:25px;color:var(--white)}
.banner .band .bottom .t{color:var(--teal)}
.banner .band .bottom .o{color:var(--orange)}

/* Card */
.card{left:612px;top:430px;width:488px;height:262px}
.card .upper{left:0;top:0;width:488px;height:150px;background:var(--orange-light);color:var(--white)}
.card .time{left:34px;top:30px;font-size:18px;font-weight:700}
.card .place{left:34px;top:62px;font-size:14px;line-height:1.45}
.card .claim{left:34px;top:160px;font-size:10px;font-weight:700;color:var(--grey);line-height:1.4}
.card .date{left:34px;top:198px;font-size:38px;color:var(--purple)}
.card .pill{width:120px;height:44px;font-size:11px}
</style>
</head>
<body>

<section class="piece poster">
  <div class="abs header">
    <div class="abs amp" aria-hidden="true">&amp;</div>
    <h1 class="abs title">Funken Fragen</h1>
    <div class="abs subtitle mono">MESSE ZÜRICH</div>
  </div>
  <div class="abs photo-cool" style="left:0;top:245px;width:176px;height:173px" role="img" aria-label="Foto: Kind mit Trommel und Kind mit Rassel vor einer Tafel"></div>
  <div class="abs brand" style="left:176px;top:245px;width:200px;height:173px">
    <span class="dot"></span>
    <span class="name">Funken und Fragen</span>
    <span class="url">www.funkenundfragen.ch</span>
  </div>
  <div class="abs photo-sun" style="left:376px;top:245px;width:184px;height:173px" role="img" aria-label="Foto: Kind blickt durch eine Kamera auf einem Stativ"></div>
  <div class="abs info">
    <div class="abs date mono">Sonntag, 9.11.2012</div>
    <div class="abs time">11 Uhr - 18.00 Uhr.</div>
    <div class="abs place">Seeforumhalle-Lindensaal,<br>Wendelgasse 7, 8047 Zürich.</div>
  </div>
  <div class="abs claim"><p>... damit Kindern ihre aktuellen und zukünftigen<br>Herausforderungen spielend meistern!</p></div>
  <div class="abs footer">www.funkenundfragen.de<br>Veranstalter: Funkenundfragen GmbH, Am Weiherhang 12, 8836 Bächtal</div>
  <div class="pill blue" style="left:415px;top:520px">Konzentration<br>fördern</div>
  <div class="pill orange" style="left:418px;top:585px">Lernen<br>entfalten</div>
  <div class="pill teal" style="left:415px;top:652px">Begabungen<br>erkennen</div>
</section>

<section class="piece banner">
  <div class="abs photo-cool" style="left:0;top:0;width:130px;height:130px" role="img" aria-label="Foto: Kinder mit Trommel und Rassel vor einer Tafel"></div>
  <div class="abs brand" style="left:130px;top:0;width:206px;height:130px">
    <span class="dot"></span>
    <span class="name" style="font-size:17px">Funken und Fragen</span>
    <span class="url" style="font-size:8px">www.funkenundfragen.ch</span>
  </div>
  <div class="abs photo-sun" style="left:336px;top:0;width:130px;height:130px" role="img" aria-label="Foto: Kind an einer Kamera auf Stativ"></div>
  <div class="abs band">
    <div class="top mono">MESSE ZÜRICH</div>
    <div class="bottom mono">"<span class="t">Funken</span>&amp;<span class="o">Fragen</span>"</div>
  </div>
</section>

<section class="piece card">
  <div class="abs upper">
    <div class="abs time">11 Uhr - 18.00 Uhr</div>
    <div class="abs place">Seeforumhalle-Lindensaal,<br>Wendelgasse 7, 8047 Zürich.</div>
  </div>
  <div class="abs claim">... damit Kindern ihre aktuellen und zukünftigen Herausforderungen<br>spielend meistern!</div>
  <div class="abs date mono">Sonntag, 9.11.2012</div>
  <div class="pill teal" style="left:382px;top:8px">Konzentration<br>fördern</div>
  <div class="pill orange" style="left:382px;top:62px">Lernen<br>entfalten</div>
  <div class="pill" style="left:382px;top:116px;background:var(--purple)">Begabungen<br>erkennen</div>
</section>

</body>
</html>
```